Need a new logo/business card for a cafe

I need a new logo and business card for a café. The café is called "Ladle", and we have a reputation for making a high quality cup of espresso coffee. I would like the business card design to reflect this "high quality". Our baristas craft our customers coffee with care to achieve this result. I would like to see designs that include a warm latte brown color. The card will be single sided to allow the rear to be used as a loyalty card which means the design will need to include space for our business address, phone number, and facebook page details. The uploaded logo is already in use on the café front window, and if it can be incorporated or used that would be great, but I am open to completely new designs as well. Thank you.
Updates
Thank you to all for the submissions. There's quite a few I like now, the hardest part will be choosing! I've set up a poll for added feedback from my own contacts and will wait on results from that.
Hello, more great designs coming in, thank you very much. There's quite a few that I really like, so my biggest challenge is going to be choosing one. Thanks again for your time, and I'll get onto the hard task of making that choice. Marcia
Industry/Entity Type
Cafe
Look and feel
Each slider illustrates characteristics of the customer's brand and the style your logo design should communicate.

```html
<!DOCTYPE html>
<html lang="en">
<head>
<meta charset="utf-8">
<title>Ladle – Business Card Variants</title>
<link href="https://fonts.googleapis.com/css2?family=Exo+2:wght@400;500&family=Audiowide&display=swap" rel="stylesheet">
<style>
  :root {
    --backdrop: #8c8c8c;
    --peach: #ecd0b8;
    --cream-left: #f5e5da;
    --cream-right: #fdfbf9;
    --wave-white: #ffffff;
    --latte-border: #8e7767;
    --latte-fill: #d8c6ba;
    --espresso: #4a3328;
    --brand-brown: #4a2a1e;
  }
  * { margin: 0; padding: 0; box-sizing: border-box; }
  html, body {
    width: 1030px;
    height: 1200px;
    overflow: hidden;
    background: var(--backdrop);
  }
  .sheet { position: relative; width: 1030px; height: 1200px; }
  .card {
    position: absolute;
    left: 86px;
    width: 860px;
    height: 469px;
  }
  .card--classic { top: 102px; }
  .card--bold { top: 628px; }
  .card-art { position: absolute; inset: 0; width: 860px; height: 469px; }
  .contact-row {
    position: absolute;
    left: 46px;
    height: 30px;
    display: flex;
    align-items: center;
    gap: 12px;
    color: var(--espresso);
    font-family: "Exo 2", sans-serif;
    font-size: 22px;
    letter-spacing: 0.5px;
  }
  .contact-row svg { width: 28px; height: 30px; flex: none; }
  .contact-row--phone { top: 66px; }
  .contact-row--mobile { top: 123px; }
  .contact-row--social { top: 175px; }
  .card--bold .contact-row {
    font-family: "Audiowide", sans-serif;
    font-size: 21px;
    color: #3a2218;
    letter-spacing: 1px;
  }
  .social-square {
    width: 26px; height: 26px;
    background: var(--espresso);
    border-radius: 2px;
    margin: 0 1px;
    flex: none;
  }
  .address {
    position: absolute;
    left: 202px;
    top: 370px;
    display: flex;
    gap: 8px;
    color: var(--espresso);
    font-family: "Exo 2", sans-serif;
    font-size: 18.5px;
    line-height: 24px;
  }
  .address svg { width: 14px; height: 20px; margin-top: 2px; flex: none; }
  .brand-name {
    position: absolute;
    left: 600px;
    top: 280px;
    width: 230px;
    text-align: center;
    font-family: "Exo 2", sans-serif;
    font-weight: 500;
    font-size: 52px;
    color: var(--brand-brown);
  }
</style>
</head>
<body>
<div class="sheet">

  <section class="card card--classic">
    <svg class="card-art" viewBox="0 0 780 425" preserveAspectRatio="none" aria-hidden="true">
      <defs>
        <linearGradient id="creamA" x1="0" x2="1" y1="0" y2="0">
          <stop offset="0" stop-color="#f5e5da"/>
          <stop offset="1" stop-color="#fdfbf9"/>
        </linearGradient>
        <clipPath id="outerA"><rect x="0" y="0" width="780" height="425" rx="14"/></clipPath>
        <clipPath id="innerA"><rect x="8" y="8" width="764" height="409" rx="8"/></clipPath>
      </defs>
      <rect x="0" y="0" width="780" height="425" rx="14" fill="var(--peach)"/>
      <rect x="8" y="8" width="764" height="409" rx="8" fill="url(#creamA)"/>
      <g clip-path="url(#outerA)">
        <path d="M0,252 C120,310 240,325 380,250 C520,170 620,100 700,112 C740,118 765,140 780,165 L780,425 L0,425 Z" fill="var(--peach)"/>
        <path d="M0,262 C120,320 240,335 380,260 C520,180 620,110 700,122 C740,128 765,150 780,175 L780,425 L0,425 Z" fill="var(--wave-white)"/>
        <path d="M0,270 C120,328 240,343 380,268 C520,188 620,118 700,130 C740,136 765,158 780,183 L780,425 L0,425 Z" fill="var(--latte-border)"/>
      </g>
      <g clip-path="url(#innerA)">
        <path d="M0,278 C120,336 240,351 380,276 C520,196 620,126 700,138 C740,144 765,166 780,191 L780,425 L0,425 Z" fill="var(--latte-fill)"/>
      </g>
    </svg>

    <div class="contact-row contact-row--phone">
      <svg viewBox="0 0 28 30"><circle cx="14" cy="15" r="12" fill="none" stroke="currentColor" stroke-width="2"/><path d="M9,9 l3,-1 2,4 -2,1.5 c1,2.5 2.5,4 5,5 l1.5,-2 4,2 -1,3 c-6,0 -12.5,-6.5 -12.5,-12.5z" fill="currentColor"/></svg>
      <span>123.456.7890</span>
    </div>
    <div class="contact-row contact-row--mobile">
      <svg viewBox="0 0 28 30"><rect x="7" y="4" width="14" height="25" rx="2" fill="none" stroke="currentColor" stroke-width="2"/><line x1="11" y1="25" x2="17" y2="25" stroke="currentColor" stroke-width="2"/><path d="M11,2 q3,-2 6,0" fill="none" stroke="currentColor" stroke-width="1.2"/></svg>
      <span>123.456.7890</span>
    </div>
    <div class="contact-row contact-row--social">
      <span class="social-square"></span>
      <span>ladlecafe.page/</span>
    </div>

    <div class="address">
      <svg viewBox="0 0 14 20"><path d="M7,1 a6,6 0 0 1 6,6 c0,5 -6,12 -6,12 s-6,-7 -6,-12 a6,6 0 0 1 6,-6z" fill="currentColor"/><circle cx="7" cy="7" r="2.2" fill="var(--latte-fill)"/></svg>
      <div>Address line 1<br>Address line 2<br>Address line 3</div>
    </div>

    <div class="brand-name">Ladle</div>
  </section>

  <section class="card card--bold">
    <svg class="card-art" viewBox="0 0 780 425" preserveAspectRatio="none" aria-hidden="true">
      <defs>
        <linearGradient id="creamB" x1="0" x2="1" y1="0" y2="0">
          <stop offset="0" stop-color="#f5e5da"/>
          <stop offset="1" stop-color="#fdfbf9"/>
        </linearGradient>
        <clipPath id="outerB"><rect x="0" y="0" width="780" height="425" rx="14"/></clipPath>
        <clipPath id="innerB"><rect x="8" y="8" width="764" height="409" rx="8"/></clipPath>
      </defs>
      <rect x="0" y="0" width="780" height="425" rx="14" fill="var(--peach)"/>
      <rect x="8" y="8" width="764" height="409" rx="8" fill="url(#creamB)"/>
      <g clip-path="url(#outerB)">
        <path d="M0,252 C120,310 240,325 380,250 C520,170 620,100 700,112 C740,118 765,140 780,165 L780,425 L0,425 Z" fill="var(--peach)"/>
        <path d="M0,262 C120,320 240,335 380,260 C520,180 620,110 700,122 C740,128 765,150 780,175 L780,425 L0,425 Z" fill="var(--wave-white)"/>
        <path d="M0,270 C120,328 240,343 380,268 C520,188 620,118 700,130 C740,136 765,158 780,183 L780,425 L0,425 Z" fill="var(--latte-border)"/>
      </g>
      <g clip-path="url(#innerB)">
        <path d="M0,278 C120,336 240,351 380,276 C520,196 620,126 700,138 C740,144 765,166 780,191 L780,425 L0,425 Z" fill="var(--latte-fill)"/>
      </g>
    </svg>

    <div class="contact-row contact-row--phone">
      <svg viewBox="0 0 28 30"><circle cx="14" cy="15" r="12" fill="none" stroke="currentColor" stroke-width="2"/><path d="M9,9 l3,-1 2,4 -2,1.5 c1,2.5 2.5,4 5,5 l1.5,-2 4,2 -1,3 c-6,0 -12.5,-6.5 -12.5,-12.5z" fill="currentColor"/></svg>
      <span>123.456.7890</span>
    </div>
    <div class="contact-row contact-row--mobile">
      <svg viewBox="0 0 28 30"><rect x="7" y="4" width="14" height="25" rx="2" fill="none" stroke="currentColor" stroke-width="2"/><line x1="11" y1="25" x2="17" y2="25" stroke="currentColor" stroke-width="2"/><path d="M11,2 q3,-2 6,0" fill="none" stroke="currentColor" stroke-width="1.2"/></svg>
      <span>123.456.7890</span>
    </div>
    <div class="contact-row contact-row--social">
      <span class="social-square"></span>
      <span>ladlecafe.page/</span>
    </div>

    <div class="address">
      <svg viewBox="0 0 14 20"><path d="M7,1 a6,6 0 0 1 6,6 c0,5 -6,12 -6,12 s-6,-7 -6,-12 a6,6 0 0 1 6,-6z" fill="currentColor"/><circle cx="7" cy="7" r="2.2" fill="var(--latte-fill)"/></svg>
      <div>Address line 1<br>Address line 2<br>Address line 3</div>
    </div>

    <div class="brand-name">Ladle</div>
  </section>

</div>
</body>
</html>
```